TalkBridge - Language Coaching Services

Sleek, innovative, trendy design for Language Coaching business.

TalkBridge is a new UK based company that provides Language Coaching services. We offer highly personalized on-line and face to face language courses. We also impart learning techniques workshops based on the latest neuroscience research for second-language acquisition.

Target Market(s)

Industry/Entity Type

Consulting

Contact Information for Business Card

TalkBridge
ElenaVT@talkbridge-demo.co.uk
TalkBridge-demo.co.uk
London, UK

Font styles to use
Sans Serif

```html
<!DOCTYPE html>
<html lang="en">
<head>
<meta charset="utf-8">
<title>TalkBridge Business Card</title>
<link href="https://fonts.googleapis.com/css2?family=Montserrat:wght@500;700&family=Open+Sans:wght@700&display=swap" rel="stylesheet">
<style>
  :root {
    --backdrop: #021a26;
    --brand-light: #0aa3dc;
    --brand-mid: #0784bd;
    --brand-deep: #045887;
    --ink: #0b5a88;
    --paper: #f6f7f8;
    --silver: #e4e6e8;
    --white: #ffffff;
  }
  * { margin: 0; padding: 0; box-sizing: border-box; }
  html, body { width: 1200px; height: 1000px; overflow: hidden; }
  body { background: var(--backdrop); position: relative; font-family: "Open Sans", Arial, sans-serif; }

  .card {
    position: absolute;
    left: 300px;
    width: 600px;
    height: 342px;
    border-radius: 22px;
    overflow: hidden;
  }
  .card-front {
    top: 115px;
    background: linear-gradient(200deg, var(--brand-light) 0%, var(--brand-mid) 45%, var(--brand-deep) 100%);
  }
  .card-back { top: 543px; background: var(--paper); }
  .card-shapes { position: absolute; inset: 0; }

  .front-mark {
    position: absolute;
    left: 234px; top: 68px;
    width: 134px; height: 134px;
    border-radius: 50%;
    border: 7px solid var(--silver);
  }
  .front-name {
    position: absolute;
    left: 0; right: 0; top: 205px;
    text-align: center;
    font-family: "Montserrat", Arial, sans-serif;
    font-weight: 500;
    font-size: 50px;
    letter-spacing: 1px;
    color: var(--silver);
  }

  .holder {
    position: absolute;
    right: 22px; top: 26px;
    font-family: "Montserrat", Arial, sans-serif;
    font-weight: 700;
    font-size: 20px;
    letter-spacing: 1px;
    color: var(--white);
  }
  .back-name {
    position: absolute;
    left: 320px; top: 72px;
    width: 260px;
    text-align: center;
    font-family: "Montserrat", Arial, sans-serif;
    font-weight: 500;
    font-size: 37px;
    color: var(--brand-mid);
  }
  .contact-list {
    position: absolute;
    left: 300px; top: 129px;
    width: 300px;
    list-style: none;
    text-align: center;
  }
  .contact-item { height: 67px; }
  .contact-icon {
    display: block;
    margin: 0 auto 6px;
    width: 26px; height: 26px;
  }
  .contact-text { font-size: 17px; font-weight: 700; color: var(--ink); }
</style>
</head>
<body>

<section class="card card-front" aria-label="Card front">
  <div class="front-mark" aria-hidden="true"></div>
  <div class="front-name">TALKBRIDGE</div>
</section>

<section class="card card-back" aria-label="Card back">
  <svg class="card-shapes" viewBox="0 0 600 342" aria-hidden="true">
    <defs>
      <linearGradient id="band-fill" x1="0" y1="0" x2="1" y2="0">
        <stop offset="0" stop-color="#0aa3dc"/>
        <stop offset="1" stop-color="#045887"/>
      </linearGradient>
      <linearGradient id="ring-fill" x1="0" y1="0" x2="1" y2="1">
        <stop offset="0" stop-color="#0aa3dc"/>
        <stop offset="1" stop-color="#045887"/>
      </linearGradient>
    </defs>
    <polygon points="245,24 600,24 600,54 277,54" fill="url(#band-fill)"/>
    <polygon points="0,286 45,286 85,318 0,318" fill="url(#band-fill)"/>
    <circle cx="165" cy="187" r="133" fill="none" stroke="url(#ring-fill)" stroke-width="15"/>
  </svg>

  <div class="holder">JOHN DOE | OWNER</div>
  <div class="back-name">TALKBRIDGE</div>

  <ul class="contact-list">
    <li class="contact-item">
      <svg class="contact-icon" viewBox="0 0 26 26" aria-hidden="true">
        <circle cx="13" cy="13" r="13" fill="#0aa3dc"/>
        <g fill="none" stroke="#fff" stroke-width="1.3">
          <circle cx="13" cy="13" r="7"/>
          <ellipse cx="13" cy="13" rx="3" ry="7"/>
          <line x1="6" y1="13" x2="20" y2="13"/>
          <line x1="7.5" y1="9.5" x2="18.5" y2="9.5"/>
          <line x1="7.5" y1="16.5" x2="18.5" y2="16.5"/>
        </g>
      </svg>
      <span class="contact-text">ElenaVT@talkbridge-demo.co.uk</span>
    </li>
    <li class="contact-item">
      <svg class="contact-icon" viewBox="0 0 26 26" aria-hidden="true">
        <circle cx="13" cy="13" r="13" fill="#0aa3dc"/>
        <g fill="none" stroke="#fff" stroke-width="1.4">
          <rect x="6.5" y="8.5" width="13" height="9"/>
          <polyline points="6.5,8.5 13,14 19.5,8.5"/>
        </g>
      </svg>
      <span class="contact-text">TalkBridge-demo.co.uk</span>
    </li>
    <li class="contact-item">
      <svg class="contact-icon" viewBox="0 0 26 26" aria-hidden="true">
        <circle cx="13" cy="13" r="13" fill="#0aa3dc"/>
        <path d="M13 20 C9 15 8.5 13 8.5 11 A4.5 4.5 0 0 1 17.5 11 C17.5 13 17 15 13 20 Z" fill="#fff"/>
        <circle cx="13" cy="11" r="1.8" fill="#0aa3dc"/>
      </svg>
      <span class="contact-text">London, UK</span>
    </li>
  </ul>
</section>

</body>
</html>
```